Onboarding Carousel UI/UX design

We need a great UI/UX design for our onboarding carousel as attached in the PDF document. The chosen designers will be given our brand book with colors and styles to be used. The images must be focused on the content of each slide and be professional unique style (Do not use the childish cartoons we have used for placeholders)

Industry/Entity Type

Mortgage Brokerage

Number of Pages Required

5+ page

Font styles to use
Other font styles liked:
• Roboto

Requirements
Must have
• Great UI / UX design
Very relevant content of the images to match the slide
Nice to have
• Brand book

https://mock.vexlin.com/view/4b7a21ce-9d05-4f1a-8e63-27c4d90a1b6f-c3d1/?fullscreen

Image styles we like. Would need to be customized and made unique for us.

https://pixmora.com/shots/7418226-Trelvo-Nubank-Illustration-Collaboration
https://kestrelhollowlab.co.za/software-client-style-frames
Should not have
• Do not use the childish images we have used as placeholders

```html
<!DOCTYPE html>
<html lang="en">
<head>
<meta charset="UTF-8">
<title>Welcome to Finance Broker</title>
<link href="https://fonts.googleapis.com/css2?family=Roboto:wght@300;400;500&display=swap" rel="stylesheet">
<style>
  :root {
    --bg-cream: #fdf8ec;
    --ink-navy: #1a1f6b;
    --text-grey: #8c8c8c;
    --text-soft: #8f8f8f;
    --text-dark: #4a4a4a;
    --brand-blue: #6589e6;
    --link-blue: #5b7fe0;
    --white: #ffffff;
    --art-blue: #dfe6f8;
    --art-warm: #f8ead0;
  }
  * { margin: 0; padding: 0; box-sizing: border-box; }
  html, body {
    width: 1200px;
    height: 2402px;
    overflow: hidden;
  }
  body {
    background: var(--bg-cream);
    font-family: "Roboto", Arial, sans-serif;
    position: relative;
  }
  .onboarding-screen {
    position: absolute;
    inset: 0;
  }
  .hero-illustration {
    position: absolute;
    left: 165px;
    top: 227px;
    width: 897px;
    height: 970px;
    border-radius: 48px;
    background: radial-gradient(ellipse at 55% 45%, var(--art-blue) 0%, var(--art-warm) 60%, var(--bg-cream) 100%);
  }
  .welcome-title {
    position: absolute;
    top: 1290px;
    left: 0;
    width: 100%;
    text-align: center;
    font-size: 84px;
    font-weight: 500;
    color: var(--ink-navy);
    letter-spacing: -0.5px;
  }
  .intro-lead {
    position: absolute;
    top: 1450px;
    left: 0;
    width: 100%;
    text-align: center;
    font-size: 49px;
    font-weight: 400;
    line-height: 70px;
    color: var(--text-grey);
  }
  .intro-note {
    position: absolute;
    top: 1709px;
    left: 0;
    width: 100%;
    text-align: center;
    font-size: 40px;
    font-weight: 300;
    line-height: 69px;
    color: var(--text-soft);
  }
  .next-button {
    position: absolute;
    left: 119px;
    top: 1863px;
    width: 967px;
    height: 127px;
    border: none;
    border-radius: 64px;
    background: var(--brand-blue);
    color: var(--white);
    font-family: "Roboto", Arial, sans-serif;
    font-size: 46px;
    font-weight: 400;
    letter-spacing: 0.5px;
  }
  .sign-in-prompt {
    position: absolute;
    top: 2093px;
    left: 0;
    width: 100%;
    text-align: center;
    font-size: 35px;
    font-weight: 400;
    color: var(--text-dark);
  }
  .sign-in-link {
    color: var(--link-blue);
    font-weight: 500;
    text-decoration: none;
  }
</style>
</head>
<body>
  <main class="onboarding-screen">
    <div class="hero-illustration" role="img" aria-label="Illustration of a cheerful man in a blue sweater holding a bank card and a phone, floating among gold dollar coins and colourful confetti shapes"></div>

    <h1 class="welcome-title">Welcome to Finance Broker</h1>

    <p class="intro-lead">You can apply online for your next<br>mortgage credit in about 20 minutes.</p>

    <p class="intro-note">It’s easy, and we will guide you all the way.<br>See the five simple steps that you have to take!</p>

    <button class="next-button" type="button">NEXT</button>

    <p class="sign-in-prompt">Already have an account? <a class="sign-in-link" href="#">Sign in</a></p>
  </main>
</body>
</html>
```